Web design required

1-We need a web design for existing company based in New Zealand
2-We build residential house and light commercial
3-We has in-house designer which allow us can provide interior design
4-We modeling project before site construction, which enable both client and construction team to visually analysis whole project,

Target Market(s)

middle class residential house market
Ref: http://www.brackwellbuilders.co.nz/

Industry/Entity Type

Construction Company

Number of Pages Required

1 page

Font styles to use
Sans Serif
Other font styles liked:
• Such as : Central Gothic or similar which has more design taste

Colors

Designer to choose colors to be used in the design.

Requirements
Must have
• Front sheet, contact information, sample project

```html
<!DOCTYPE html>
<html lang="en">
<head>
<meta charset="utf-8">
<title>Kestrel Homes</title>
<link href="https://fonts.googleapis.com/css2?family=Montserrat:wght@400;600;700&family=Open+Sans:wght@400;600;700&family=Marcellus&display=swap" rel="stylesheet">
<style>
:root{
  --blue:#0a63b8;
  --blue-dark:#07509a;
  --ink:#222;
  --text:#555;
  --muted:#888;
  --faint:#e6e6e6;
  --light-bg:#eeeeee;
  --dark:#2a2d31;
  --contact-bg:#4b4b4b;
  --footer-bg:#333;
  --white:#fff;
}
*{box-sizing:border-box;margin:0;padding:0}
html,body{width:1200px;height:4045px;overflow:hidden}
body{position:relative;font-family:"Open Sans",sans-serif;color:var(--text);background:var(--white)}
.abs{position:absolute}

/* header */
.site-header{left:0;top:0;width:1200px;height:94px;background:var(--white)}
.brand{left:67px;top:22px;display:flex;align-items:center;gap:12px}
.brand-mark{width:46px;height:46px;border-radius:50%;background:var(--blue)}
.brand-name{font-family:"Montserrat",sans-serif;font-weight:700;font-size:28px;color:#333;letter-spacing:1px}
.main-nav{right:68px;top:36px;display:flex;gap:34px;font-family:"Montserrat",sans-serif;font-size:15px;color:#333}
.main-nav .active{position:relative}
.main-nav .active::before{content:"";position:absolute;left:0;right:0;top:-36px;height:6px;background:var(--blue)}

/* hero */
.hero{left:0;top:94px;width:1200px;height:594px;background:linear-gradient(180deg,#9fb3bd 0%,#6e7f88 45%,#3d4348 100%)}
.hero-title{left:67px;top:258px;font-family:"Montserrat",sans-serif;font-weight:700;font-size:54px;line-height:58px;color:var(--white);letter-spacing:1px}
.hero-dots{left:1126px;top:222px;width:6px}
.hero-dots span{display:block;width:6px;height:6px;background:var(--white);border-radius:50%;margin-bottom:6px}

.guide-line{background:var(--blue);width:3px}

/* section labels */
.ghost{font-family:"Montserrat",sans-serif;font-weight:400;font-size:76px;color:var(--faint);letter-spacing:2px;line-height:1}
.sec-title{font-family:"Montserrat",sans-serif;font-weight:700;font-size:27px;color:var(--ink);line-height:34px}
.body-copy{font-size:14.5px;line-height:23px;color:var(--text)}
.body-copy p+p{margin-top:22px}

.photo{display:block}
.read-more{left:701px;top:1143px;width:138px;height:49px;border:2px solid var(--blue);color:var(--blue);font-family:"Montserrat",sans-serif;font-weight:600;font-size:15px;display:flex;align-items:center;justify-content:center}
.slide-arrows{left:556px;top:916px;display:flex;gap:6px}
.slide-arrows span{width:44px;height:56px;border:1px solid #ddd;background:rgba(255,255,255,.75);display:flex;align-items:center;justify-content:center}

/* services */
.services-band{left:0;top:1375px;width:1200px;height:440px;background:var(--light-bg)}
.service{width:300px}
.service h4{font-family:"Montserrat",sans-serif;font-weight:700;font-size:14px;color:var(--ink);margin-top:8px}
.service .rule{width:54px;height:2px;background:var(--blue);margin:12px 0 14px}
.service p{font-size:13.5px;line-height:22px;color:var(--muted)}

/* team */
.team{left:0;top:2117px;width:1200px;height:607px;background:linear-gradient(180deg,#2e3338,#1e2226)}
.team .ghost{color:rgba(255,255,255,.12)}
.team-title{color:var(--white)}
.member{width:237px;height:351px;border:4px solid #6c6c6c;background:linear-gradient(180deg,#8a8a82,#5b5e60)}
.member .name-bar{position:absolute;left:0;right:0;bottom:0;height:54px;background:rgba(70,70,70,.85);color:var(--white);font-family:"Montserrat",sans-serif;font-weight:600;font-size:20px;display:flex;align-items:center;justify-content:center}
.member.featured{border-color:#e8e8e8}
.member.featured .info{position:absolute;left:0;right:0;bottom:0;height:164px;background:var(--blue);color:var(--white);text-align:center;padding:10px 12px 0}
.member.featured .info h5{font-family:"Montserrat",sans-serif;font-weight:600;font-size:20px}
.member.featured .info p{font-size:12.5px;line-height:18px;font-weight:700;margin-top:6px}
.socials{display:flex;justify-content:center;gap:8px;margin-top:10px}
.socials span{width:28px;height:28px;border-radius:50%;background:var(--white)}

/* offer & feedback */
.offer{left:67px;top:2816px;width:548px;height:447px;background:var(--blue);color:var(--white);padding:26px 30px}
.offer h3{font-family:"Montserrat",sans-serif;font-weight:700;font-size:26px}
.offer-grid{display:grid;grid-template-columns:1fr 1fr;row-gap:38px;column-gap:24px;margin-top:34px}
.offer-item{display:flex;gap:16px}
.offer-item .ic{width:38px;height:38px;flex:none;border:2px solid rgba(255,255,255,.85)}
.offer-item h6{font-family:"Montserrat",sans-serif;font-weight:700;font-size:15px}
.offer-item p{font-size:13px;line-height:17px;margin-top:2px}
.feedback{left:572px;top:2940px;width:534px;height:472px;background:var(--light-bg);padding:48px 60px 0 84px}
.feedback h3{font-family:"Montserrat",sans-serif;font-weight:600;font-size:26px;color:#333;line-height:34px}
.feedback .quote-mark{font-family:"Marcellus",serif;font-size:90px;color:#ddd;line-height:1;position:absolute;left:84px;top:120px}
.feedback .body-copy{margin-top:50px;font-size:14px;line-height:23px}
.feedback .author{text-align:right;margin-top:34px;font-size:13px;line-height:20px;color:var(--muted)}
.feedback .author b{display:block;color:var(--blue);font-weight:700;margin-bottom:4px}

/* contact */
.contact{left:0;top:3506px;width:1200px;height:472px;background:var(--contact-bg);color:var(--white)}
.contact h2{position:absolute;left:84px;top:82px;font-family:"Marcellus",serif;font-weight:400;font-size:37px;letter-spacing:2px}
.contact .intro{position:absolute;left:84px;top:128px;font-size:14.5px;line-height:19px;width:560px}
.contact-item{position:absolute;left:78px;display:flex;align-items:center;gap:20px;font-size:14px;line-height:18px}
.contact-item .ic{width:42px;height:42px;border-radius:50%;background:var(--white);display:flex;align-items:center;justify-content:center;flex:none}
.field{position:absolute;border:1px solid #cfcfcf;color:var(--white);font-size:14px;padding:10px 12px}
.submit{position:absolute;left:494px;top:383px;width:113px;height:41px;background:#1f1f1f;color:var(--white);font-family:"Montserrat",sans-serif;font-size:14px;display:flex;align-items:center;justify-content:center}
.site-footer{left:0;top:3978px;width:1200px;height:67px;background:var(--footer-bg);color:#ddd;font-size:14px;display:flex;align-items:center;justify-content:center}
</style>
</head>
<body>

<header class="abs site-header">
  <div class="abs brand"><span class="brand-mark"></span><span class="brand-name">KESTREL HOMES</span></div>
  <nav class="abs main-nav">
    <span class="active">HOME</span><span>ABOUT</span><span>WHO ARE YOU</span><span>SERVICE</span><span>OUR WORK</span><span>NEWS</span><span>CONTACT US</span>
  </nav>
</header>

<section class="abs hero" role="img" aria-label="Tower cranes above a high-rise under construction against a hazy sky"></section>
<h1 class="abs hero-title">RELENTLESSLY<br>PROACTIVE..</h1>
<div class="abs hero-dots"><span></span><span></span><span></span></div>

<!-- blue guide line with markers -->
<div class="abs guide-line" style="left:187px;top:400px;height:248px"></div>
<svg class="abs" style="left:162px;top:648px" width="54" height="160" viewBox="0 0 54 160">
  <rect width="54" height="160" fill="#0a63b8"/>
  <path d="M20 22 L27 29 L34 22" fill="none" stroke="#fff" stroke-width="2.5"/>
</svg>
<svg class="abs" style="left:162px;top:1160px" width="54" height="178" viewBox="0 0 54 178">
  <path d="M0 0 H54 V150 L27 178 L0 150 Z" fill="#0a63b8"/>
</svg>
<div class="abs guide-line" style="left:187px;top:1338px;height:92px"></div>

<!-- featured projects -->
<div class="abs ghost" style="left:553px;top:748px">FEATURED</div>
<h2 class="abs sec-title" style="left:698px;top:780px">FEATURED<br>PROJECTS</h2>
<svg class="abs" style="left:764px;top:862px" width="22" height="18" viewBox="0 0 22 18"><path d="M2 16 H20 M4 16 V9 L11 4 L18 9 V16" fill="none" stroke="#0a63b8" stroke-width="2"/></svg>
<div class="abs body-copy" style="left:698px;top:900px;width:424px">
  <p>Lorem Ipsum is simply dummy text of the printing and typesetting industry. Lorem Ipsum has been the industry's standard dummy text ever since the 1500s, when an unknown printer took a galley of type and scrambled it to make a type specimen book. It has survived not only five centuries,</p>
  <p>but also the leap into electronic typesetting, remaining essentially unchanged. It was popularised in the 1960s with the release of Letraset sheets containing Lorem Ipsum passages, and more recently with desktop publishing</p>
</div>
<div class="abs read-more">Read More&nbsp;&nbsp;»</div>
<div class="abs photo" style="left:67px;top:804px;width:486px;height:356px;background:linear-gradient(135deg,#e7c23a 0%,#9fb8d6 45%,#5f7ea3 100%)" role="img" aria-label="Yellow hard hat resting on rolled building plans"></div>
<div class="abs photo" style="left:359px;top:984px;width:296px;height:256px;background:linear-gradient(160deg,#7a8ea3 0%,#3d5a86 60%,#e0b730 100%);border:4px solid #fff" role="img" aria-label="Builder in a hard hat on a construction site"></div>
<div class="abs slide-arrows">
  <span><svg width="14" height="20"><path d="M10 3 L3 10 L10 17" fill="none" stroke="#999" stroke-width="2"/></svg></span>
  <span><svg width="14" height="20"><path d="M4 3 L11 10 L4 17" fill="none" stroke="#999" stroke-width="2"/></svg></span>
</div>

<!-- services -->
<div class="abs services-band"></div>
<div class="abs photo" style="left:612px;top:1340px;width:494px;height:451px;background:linear-gradient(170deg,#c7d4e2 0%,#7d8c9d 50%,#3b4b73 100%)" role="img" aria-label="Two engineers in hard hats reviewing work beside a building frame"></div>
<div class="abs ghost" style="left:80px;top:1458px">SERVICES</div>
<h2 class="abs sec-title" style="left:116px;top:1505px">OUR SERVICES</h2>
<div class="abs body-copy" style="left:89px;top:1565px;width:425px">
  <p>Lorem Ipsum is simply dummy text of the printing and typesetting industry. Lorem Ipsum has been the industry's standard dummy text ever since the 1500s, when an unknown printer took a galley of type and scrambled it to make a type specimen book. It has survived not only five centuries,</p>
  <p>but also the leap into electronic typesetting, remaining essentially unchanged. It was popularised in the 1960s with the release of Letraset sheets containing Lorem Ipsum passages, and more recently with desktop publishing</p>
</div>

<div class="abs service" style="left:94px;top:1868px">
  <svg width="40" height="40" viewBox="0 0 40 40"><path d="M4 36 H36 M8 36 V16 H18 V36 M18 36 V8 H32 V36 M22 14 H28 M22 20 H28 M22 26 H28" fill="none" stroke="#0a63b8" stroke-width="2.5"/></svg>
  <h4>COMMERCIAL</h4><div class="rule"></div>
  <p>Lorem Ipsum is simply dummy text of the printing and typesetting industry. Lorem Ipsum has been the industry's standard dummy text ever since the 1500s.</p>
</div>
<div class="abs service" style="left:440px;top:1868px">
  <svg width="40" height="40" viewBox="0 0 40 40"><g fill="#0a63b8"><rect x="4" y="6" width="14" height="6"/><rect x="21" y="6" width="14" height="6"/><rect x="12" y="15" width="14" height="6"/><rect x="4" y="24" width="14" height="6"/><rect x="21" y="24" width="14" height="6"/><rect x="12" y="33" width="14" height="5"/></g></svg>
  <h4>RESTORATION</h4><div class="rule"></div>
  <p>Lorem Ipsum is simply dummy text of the printing and typesetting industry. Lorem Ipsum has been the industry's standard dummy text ever since the 1500s.</p>
</div>
<div class="abs service" style="left:793px;top:1868px">
  <svg width="40" height="40" viewBox="0 0 40 40"><rect x="4" y="6" width="32" height="20" fill="none" stroke="#0a63b8" stroke-width="2.5"/><path d="M14 34 H26 M20 26 V34" stroke="#0a63b8" stroke-width="2.5"/><path d="M10 18 L16 12 L22 17 L30 10" fill="none" stroke="#0a63b8" stroke-width="2"/></svg>
  <h4>ENVIRONMENTAL</h4><div class="rule"></div>
  <p>Lorem Ipsum is simply dummy text of the printing and typesetting industry. Lorem Ipsum has been the industry's standard dummy text ever since the 1500s.</p>
</div>

<!-- team -->
<section class="abs team">
  <div class="abs ghost" style="left:70px;top:42px">TEAM</div>
  <h2 class="abs sec-title team-title" style="left:100px;top:82px">OUR TEAM</h2>
  <div class="abs member featured" style="left:67px;top:175px">
    <div class="abs" style="left:0;top:0;right:0;height:179px;background:linear-gradient(180deg,#7e9ab8,#9f8068)" role="img" aria-label="Portrait of a smiling team member"></div>
    <div class="info">
      <h5>Sam Tane</h5>
      <p>Lorem Ipsum is simply dummy text of the printing and typesetting industry. Lorem Ipsum has been the industry</p>
      <div class="socials"><span></span><span></span><span></span><span></span><span></span></div>
    </div>
  </div>
  <div class="abs member" style="left:342px;top:175px" role="img" aria-label="Portrait of a worker in a hard hat and safety vest"><div class="name-bar">Sam Tane</div></div>
  <div class="abs member" style="left:617px;top:175px" role="img" aria-label="Portrait of a carpenter in a work apron"><div class="name-bar">Sam Tane</div></div>
  <div class="abs member" style="left:892px;top:175px" role="img" aria-label="Portrait of a builder in a yellow hard hat"><div class="name-bar">Sam Tane</div></div>
</section>
<div class="abs" style="left:983px;top:2077px;width:3px;height:160px;background:var(--blue)"></div>

<!-- principal -->
<div class="abs ghost" style="left:428px;top:2770px">PRINCIPAL</div>
<div class="abs" style="left:998px;top:2724px;width:3px;height:150px;background:var(--blue)"></div>
<svg class="abs" style="left:970px;top:2868px" width="60" height="72" viewBox="0 0 60 72"><path d="M0 22 L30 0 L60 22 V72 H0 Z" fill="#0a63b8"/></svg>

<div class="abs offer">
  <h3>what we offer?</h3>
  <div class="offer-grid">
    <div class="offer-item"><span class="ic"></span><div><h6>Construction</h6><p>Lorem Ipsum dolor sit amet consectetur adipiscing</p></div></div>
    <div class="offer-item"><span class="ic"></span><div><h6>Awesome Stuff</h6><p>Lorem Ipsum dolor sit amet consectetur adipiscing</p></div></div>
    <div class="offer-item"><span class="ic"></span><div><h6>Maintanance</h6><p>Lorem Ipsum dolor sit amet consectetur adipiscing</p></div></div>
    <div class="offer-item"><span class="ic"></span><div><h6>Maintanance</h6><p>Lorem Ipsum dolor sit amet consectetur adipiscing</p></div></div>
    <div class="offer-item"><span class="ic"></span><div><h6>Good Planning</h6><p>Lorem Ipsum dolor sit amet consectetur adipiscing</p></div></div>
    <div class="offer-item"><span class="ic"></span><div><h6>Good Planning</h6><p>Lorem Ipsum dolor sit amet consectetur adipiscing</p></div></div>
  </div>
</div>

<div class="abs feedback">
  <h3>Coustomer<br>Feedback</h3>
  <span class="quote-mark">“</span>
  <div class="body-copy">Lorem Ipsum is simply dummy text of the printing and typesetting industry. Lorem Ipsum has been the industry's standard dummy text ever since the 1500s.Lorem Ipsum is simply dummy text of the printing and typesetting industry. Lorem Ipsum has been the industry's standard dummy text ever since the 1500s.</div>
  <div class="author"><b>Mere Walker</b>Was. Our multiply winged divided, him<br>Saw darkness make be whales don't and<br>land fifth great</div>
</div>

<svg class="abs" style="left:970px;top:3412px" width="60" height="70" viewBox="0 0 60 70"><path d="M0 0 H60 V48 L30 70 L0 48 Z" fill="#0a63b8"/></svg>
<div class="abs" style="left:998px;top:3482px;width:3px;height:110px;background:var(--blue)"></div>

<!-- contact -->
<section class="abs contact">
  <h2>GET IN TOUCH</h2>
  <p class="intro">We are very approachable and would love to speak to you. Feel free to call, send us an email, Tweet us or simply complete the enquiry form.</p>
  <div class="contact-item" style="top:203px">
    <span class="ic"><svg width="18" height="22" viewBox="0 0 18 22"><path d="M9 21 C9 21 2 13 2 8 A7 7 0 0 1 16 8 C16 13 9 21 9 21 Z" fill="#4b4b4b"/><circle cx="9" cy="8" r="2.6" fill="#fff"/></svg></span>
    <span>Hamilton, Waikato, offering services<br>region wide</span>
  </div>
  <div class="contact-item" style="top:274px">
    <span class="ic"><svg width="20" height="16" viewBox="0 0 20 16"><rect x="1" y="1" width="18" height="14" fill="none" stroke="#4b4b4b" stroke-width="2"/><path d="M1 2 L10 9 L19 2" fill="none" stroke="#4b4b4b" stroke-width="2"/></svg></span>
    <span>hello@kestrelhomes.co.nz</span>
  </div>
  <div class="contact-item" style="top:345px">
    <span class="ic"><svg width="18" height="18" viewBox="0 0 18 18"><path d="M3 1 L7 1 L8 5 L6 7 C7 9 9 11 11 12 L13 10 L17 11 L17 15 C17 16 16 17 15 17 C7 17 1 11 1 3 C1 2 2 1 3 1 Z" fill="#4b4b4b"/></svg></span>
    <span>+64 7 555 0142</span>
  </div>
  <div class="field" style="left:494px;top:216px;width:264px;height:43px">Name</div>
  <div class="field" style="left:494px;top:270px;width:264px;height:43px">Number</div>
  <div class="field" style="left:494px;top:324px;width:264px;height:43px">Mail</div>
  <div class="field" style="left:779px;top:216px;width:316px;height:151px">Message</div>
  <div class="submit">SUBMIT</div>
</section>

<footer class="abs site-footer">All rights reserved Copyright © 2017 Kestrel Homes Ltd</footer>

</body>
</html>
```